Design a Brochure for Famous Jewelry Brand

Design a Brochure for famous Jewelry Brand
- should be luxury
- clean and bright
- A4 Portrait type
- Edit photos in one color style

Please see attachment as guideline for layout, all the high-resolution will be provided.

```html
<!DOCTYPE html>
<html lang="en">
<head>
<meta charset="utf-8">
<title>Velmora Jewellery Brochure</title>
<link href="https://fonts.googleapis.com/css2?family=Arimo:wght@400;700&family=Cormorant+Garamond:wght@400;500&display=swap" rel="stylesheet">
<style>
  :root {
    --canvas-bg: #e4e4e4;
    --page-light: #f7f7f7;
    --page-shade: #e2e2e2;
    --ink: #1d1d1d;
    --gold: #8a6a34;
    --cream: #f2ece2;
    --photo-light: #b08c6c;
    --photo-mid: #6e4e38;
    --photo-dark: #2e211a;
    --band: rgba(28, 18, 12, 0.72);
    --ruby: rgba(176, 48, 86, 0.55);
    --ruby-soft: rgba(214, 150, 170, 0.28);
  }
  * { margin: 0; padding: 0; box-sizing: border-box; }
  html, body { width: 1200px; height: 847px; overflow: hidden; }
  body {
    background: var(--canvas-bg);
    font-family: "Arimo", Arial, sans-serif;
    color: var(--ink);
    position: relative;
  }
  .spread {
    position: absolute;
    left: 60px; top: 41px;
    width: 1080px; height: 764px;
    display: flex;
    box-shadow: 0 10px 30px rgba(0,0,0,0.18);
  }
  .page { position: relative; width: 540px; height: 764px; overflow: hidden; }

  /* Back page */
  .page--back {
    background: linear-gradient(100deg, var(--page-light) 0%, #fbfbfb 55%, var(--page-shade) 100%);
  }
  .brand {
    position: absolute;
    left: 110px; top: 118px;
    display: flex; align-items: center; gap: 14px;
  }
  .brand__dot {
    width: 44px; height: 44px; border-radius: 50%;
    background: var(--gold);
    flex: none;
  }
  .brand__name {
    font-family: "Cormorant Garamond", Georgia, serif;
    font-weight: 500;
    font-size: 40px;
    color: var(--gold);
    letter-spacing: 0.5px;
    white-space: nowrap;
  }
  .contact { position: absolute; left: 112px; top: 196px; width: 320px; }
  .contact__title { font-size: 24px; font-weight: 400; margin-bottom: 12px; }
  .contact__label { font-size: 11px; font-weight: 700; margin-bottom: 3px; }
  .contact__line { font-size: 10.5px; line-height: 1.5; white-space: nowrap; }
  .contact__group { margin-bottom: 20px; }

  .jewel-photo {
    position: absolute;
    left: 40px; top: 440px;
    width: 330px; height: 190px;
  }
  .jewel-photo__piece {
    position: absolute;
    left: 0; top: 0;
    width: 330px; height: 110px;
    border-radius: 50%;
    background: radial-gradient(closest-side, var(--ruby) 0%, var(--ruby-soft) 55%, rgba(247,247,247,0) 100%);
  }
  .jewel-photo__reflection {
    position: absolute;
    left: 20px; top: 104px;
    width: 290px; height: 70px;
    border-radius: 50%;
    background: radial-gradient(closest-side, rgba(214,150,170,0.22) 0%, rgba(247,247,247,0) 100%);
  }

  /* Cover page */
  .page--cover {
    background: linear-gradient(160deg, var(--photo-light) 0%, var(--photo-mid) 45%, var(--photo-dark) 100%);
  }
  .cover-photo {
    position: absolute; inset: 0;
    background: radial-gradient(ellipse at 35% 25%, rgba(214,180,150,0.55) 0%, rgba(110,78,56,0) 60%);
  }
  .cover-band {
    position: absolute; left: 0; right: 0;
    top: 440px; height: 66px;
    background: var(--band);
    display: flex; align-items: center; justify-content: center; gap: 12px;
  }
  .cover-band .brand__dot { width: 36px; height: 36px; }
  .cover-band .brand__name { font-size: 34px; color: #b8935a; }
  .cover-text {
    position: absolute; left: 0; right: 0; top: 530px;
    text-align: center; color: var(--cream);
  }
  .cover-text__brand { font-size: 15px; letter-spacing: 1.5px; margin-bottom: 6px; }
  .cover-text__title {
    font-family: "Cormorant Garamond", Georgia, serif;
    font-size: 46px; font-weight: 400; line-height: 1.05;
  }
  .cover-text__offer { font-size: 13px; margin-top: 8px; letter-spacing: 0.3px; }
</style>
</head>
<body>
  <main class="spread">
    <section class="page page--back">
      <div class="brand">
        <span class="brand__dot"></span>
        <span class="brand__name">Velmora</span>
      </div>
      <div class="contact">
        <h2 class="contact__title">Contact Us</h2>
        <div class="contact__group">
          <p class="contact__label">Our boutique</p>
          <p class="contact__line">Linden avenue 412, Crescent Mall, 2nd floor</p>
          <p class="contact__line">+000 50 4127730</p>
        </div>
        <div class="contact__group">
          <p class="contact__label">Vip</p>
          <p class="contact__line">Harbor Row str. 18/22</p>
          <p class="contact__line">+000 51 9052216</p>
        </div>
      </div>
      <div class="jewel-photo" role="img" aria-label="Photo of a ruby and diamond flower bracelet with reflection">
        <div class="jewel-photo__piece"></div>
        <div class="jewel-photo__reflection"></div>
      </div>
    </section>

    <section class="page page--cover">
      <div class="cover-photo" role="img" aria-label="Sepia-toned fashion photo of a model wearing a large filigree gold earring and ring"></div>
      <div class="cover-band">
        <span class="brand__dot"></span>
        <span class="brand__name">Velmora</span>
      </div>
      <div class="cover-text">
        <p class="cover-text__brand">VELMORA JEWELLERY</p>
        <h1 class="cover-text__title">Latest Collection</h1>
        <p class="cover-text__offer">Special Offers For Limited Time</p>
      </div>
    </section>
  </main>
</body>
</html>
```